Car Lubricant /Coolant Label

We are starting a bottling plant to manufacture, bottle, label and sell car coolants and Lubricants outside the united states. The name of the comp...

Industry/Entity Type

Manufacture

```html
<!DOCTYPE html>
<html lang="en">
<head>
<meta charset="utf-8">
<title>Velotherm Coolant Label</title>
<link href="https://fonts.googleapis.com/css2?family=Exo+2:ital,wght@0,500;0,600;0,700;0,800;1,700;1,800&display=swap" rel="stylesheet">
<style>
  :root {
    --page: #7d7e82;
    --label-dark: #1d1e20;
    --label-dark-2: #2b2c2f;
    --silver: #c9cbcf;
    --silver-dark: #8d9096;
    --brand-yellow: #f7d52a;
    --ink: #0c0c0c;
    --navy: #12226b;
    --navy-dark: #0a1445;
    --red: #c0101d;
    --white: #ffffff;
    --band-grey: #5a5b5f;
    --coolant-green: #2fb83a;
  }
  * { box-sizing: border-box; margin: 0; padding: 0; }
  html, body {
    width: 817px; height: 1200px; overflow: hidden;
    background: var(--page);
    font-family: "Exo 2", "Arial", sans-serif;
  }
  .canvas { position: relative; width: 817px; height: 1200px; }
  .label {
    position: absolute; left: 35px; top: 155px;
    width: 747px; height: 891px;
    border-radius: 36px;
    border: 6px solid var(--silver);
    box-shadow: inset 0 0 0 2px var(--silver-dark);
    background: linear-gradient(160deg, var(--label-dark-2), var(--label-dark) 60%);
    overflow: hidden;
  }
  .label > * { position: absolute; white-space: nowrap; }
  .shapes { left: 0; top: 0; width: 747px; height: 891px; }
  .brand-name {
    left: 45px; top: 58px;
    font-size: 92px; font-weight: 800; line-height: 1;
    color: var(--brand-yellow);
  }
  .product-name {
    left: 45px; top: 196px;
    font-size: 64px; font-weight: 800; font-style: italic; line-height: 1;
    color: var(--ink);
  }
  .product-use {
    left: 45px; top: 272px;
    font-size: 48px; font-weight: 800; line-height: 1;
    color: var(--ink);
  }
  .product-benefits {
    left: 45px; top: 342px;
    font-size: 24px; font-weight: 700; line-height: 1.12;
    color: var(--ink);
  }
  .formula-badge {
    left: 279px; top: 333px; width: 441px; height: 60px;
    border-radius: 12px;
    border: 3px solid var(--silver);
    background: linear-gradient(180deg, var(--navy), var(--navy-dark));
    color: var(--white);
    font-size: 36px; font-weight: 700;
    display: flex; align-items: center; justify-content: center;
  }
  .water-note {
    left: 14px; top: 414px;
    font-size: 27px; font-weight: 800; font-style: italic; line-height: 36px;
    color: var(--white);
  }
  .fitment-gold {
    left: 325px; top: 410px;
    font-size: 27px; font-weight: 700; line-height: 36px;
    color: var(--ink);
  }
  .usage-band {
    left: 0; top: 482px; width: 747px; height: 52px;
    background: linear-gradient(180deg, #77787c, var(--band-grey) 55%, #3f4043);
    border-top: 2px solid var(--silver);
    border-bottom: 2px solid var(--silver);
    display: flex; align-items: center; justify-content: center;
    color: var(--brand-yellow);
    font-size: 32px; font-weight: 800; font-style: italic;
    text-shadow: 2px 2px 0 #111;
  }
  .pour-visual {
    left: 0; top: 556px; width: 370px; height: 335px;
    background:
      radial-gradient(ellipse at 70% 75%, var(--coolant-green) 0%, rgba(47,184,58,0.6) 25%, transparent 50%),
      linear-gradient(135deg, #e3e5e8 0%, #a9acb1 40%, #5d6064 75%, #2a2b2e 100%);
  }
  .service-life {
    left: 372px; top: 541px;
    font-size: 32px; font-weight: 700; line-height: 1;
    color: var(--brand-yellow);
  }
  .fitment-tab {
    left: 360px; top: 590px; width: 372px; height: 38px;
    background: var(--red);
    clip-path: polygon(14px 0, 100% 0, 100% 100%, 0 100%);
    border-right: 3px solid var(--silver);
    color: var(--white);
    font-size: 27px; font-weight: 700; font-style: italic;
    display: flex; align-items: center; justify-content: center;
  }
  .formulated-for {
    left: 356px; top: 646px;
    font-size: 31px; font-weight: 600; line-height: 1;
    color: var(--white);
  }
  .markets {
    left: 384px; top: 688px;
    font-size: 32px; font-weight: 700; line-height: 40px;
    color: var(--brand-yellow);
  }
  .net-contents {
    left: 420px; top: 806px; width: 300px;
    font-size: 17px; font-weight: 500; line-height: 26px;
    color: var(--white); text-align: center;
  }
</style>
</head>
<body>
<main class="canvas">
  <section class="label">
    <svg class="shapes" viewBox="0 0 747 891" aria-hidden="true">
      <defs>
        <linearGradient id="goldFill" x1="0" y1="0" x2="0" y2="1">
          <stop offset="0" stop-color="#f6d27a"/>
          <stop offset="0.45" stop-color="#d9a23a"/>
          <stop offset="1" stop-color="#b07a1c"/>
        </linearGradient>
        <linearGradient id="blueFill" x1="0" y1="0" x2="0" y2="1">
          <stop offset="0" stop-color="#2a4fb0"/>
          <stop offset="1" stop-color="#0f276e"/>
        </linearGradient>
      </defs>
      <polygon class="gold-banner" points="0,180 441,180 495,238 747,238 747,460 306,460 292,410 0,410" fill="url(#goldFill)"/>
      <polyline points="0,180 441,180 495,238 747,238" fill="none" stroke="#eee" stroke-width="3"/>
      <polygon class="water-tab" points="0,410 300,410 285,456 0,456" fill="url(#blueFill)" stroke="#d0d2d6" stroke-width="2"/>
    </svg>

    <div class="brand-name">VELOTHERM</div>
    <div class="product-name">COOLANT</div>
    <div class="product-use">READY TO USE</div>
    <div class="product-benefits">anti boil<br>anti corrosion</div>
    <div class="formula-badge">ORIGINAL FORMULA</div>
    <div class="water-note">Do not add Water</div>
    <div class="fitment-gold">For all makes &amp; models</div>

    <div class="usage-band">Coolant for Cars, Heavy Trucks and Buses</div>

    <div class="pour-visual" role="img" aria-label="Green coolant pouring from a silver metal can"></div>

    <div class="service-life">2 year or 350,000 KMS</div>
    <div class="fitment-tab">For all makes &amp; models</div>
    <div class="formulated-for">Specially formulated for</div>
    <div class="markets">Asian, American, and<br>European cars</div>
    <div class="net-contents">1 U.S. GALLON/CONT.NET.<br>3.0L / 0.79 US Gallons</div>
  </section>
</main>
</body>
</html>
```